The Linden Clinic. Psychotherapy practice. Looking for a multi-use design.

Hello, we need someone who can give us a design that's usable across business cards, rack cards and headed paper.
We're also looking for a logo that can be used on the cards and on the web site when we change the web site.
The current web site, www.the-linden-clinic-example.co.uk can be used to gather info, but does not need to be used for colour/design choices (e.g. one partner likes the Times font another prefers a sans-serif font. One likes the idea of a brass plaque in the design, the other doesn't).
The main point about the design is that it should convey an image of a professional service - their latest strap line is "Professional • Experienced • Confidential" used in a local ad.
Updates
The ladies have also asked me to add that although the Practice is very close to Corvell Minster, and one of the lines they use on the site is "Just a few steps from the Minster", they don't want it to look like something that's Christian or religious.
Thanks.
Industry/Entity Type
Professional Service
Look and feel
Each slider illustrates characteristics of the customer's brand and the style your logo design should communicate.

```html
<!DOCTYPE html>
<html lang="en">
<head>
<meta charset="utf-8">
<title>The Linden Clinic – Identity Board</title>
<link rel="stylesheet" href="https://fonts.googleapis.com/css2?family=Fira+Sans+Condensed:wght@500&family=Heebo:wght@300&family=Pinyon+Script&family=PT+Sans+Narrow:wght@400&family=PT+Sans:ital@1&display=swap">
<style>
  :root {
    --board-bg: #f1f1f1;
    --board-light: #fafafa;
    --ink-brown: #4e3127;
    --ink-dark: #1c1c1c;
    --tagline-rose: #b2557c;
    --front-gold: #d2c46e;
    --front-gold-edge: #b29548;
    --back-rose: #b3737f;
    --back-rose-edge: #9c5f55;
    --back-cream: #f5e6cf;
    --back-ink: #4a2c25;
    --ornament-brown: #6b4a3c;
  }
  * { box-sizing: border-box; margin: 0; padding: 0; }
  html, body { width: 1200px; height: 900px; overflow: hidden; }
  body {
    position: relative;
    background: linear-gradient(120deg, var(--board-bg) 0%, var(--board-light) 45%, var(--board-bg) 100%);
    font-family: "PT Sans Narrow", "Arial Narrow", sans-serif;
  }

  .board-label {
    position: absolute;
    font-family: "Fira Sans Condensed", "Arial Narrow", sans-serif;
    font-weight: 500;
    font-size: 21px;
    color: var(--ink-dark);
  }
  .board-label--logo  { left: 1049px; top: 198px; }
  .board-label--front { left: 128px;  top: 424px; }
  .board-label--back  { right: 113px; top: 424px; }

  /* Master logo */
  .logo-art {
    position: absolute;
    left: 155px; top: 60px;
    width: 340px; height: 320px;
    border-radius: 46% 54% 50% 50%;
    background: radial-gradient(ellipse at 55% 45%, rgba(107,74,60,0.22), rgba(107,74,60,0.06) 70%, rgba(107,74,60,0));
  }
  .logo-name {
    position: absolute;
    left: 432px; top: 188px;
    font-family: "Heebo", sans-serif;
    font-weight: 300;
    font-size: 54px;
    line-height: 1;
    color: var(--ink-brown);
    white-space: nowrap;
  }
  .logo-tagline {
    position: absolute;
    left: 455px; top: 252px;
    font-family: "Heebo", sans-serif;
    font-weight: 300;
    font-size: 36px;
    line-height: 1;
    color: var(--tagline-rose);
    white-space: nowrap;
  }

  /* Business cards */
  .card {
    position: absolute;
    top: 451px;
    width: 458px; height: 255px;
    overflow: hidden;
  }
  .card--front {
    left: 128px;
    background: radial-gradient(ellipse at 60% 30%, var(--front-gold) 0%, #c9b262 55%, var(--front-gold-edge) 100%);
  }
  .card--back {
    left: 629px;
    background: radial-gradient(ellipse at 60% 20%, var(--back-rose) 0%, #ac6c72 50%, var(--back-rose-edge) 100%);
  }

  .card-front__art {
    position: absolute;
    left: 8px; top: 30px;
    width: 196px; height: 185px;
    border-radius: 50%;
    background: radial-gradient(ellipse at 55% 45%, rgba(90,62,40,0.25), rgba(90,62,40,0.05) 70%, rgba(90,62,40,0));
  }
  .card-front__name {
    position: absolute;
    left: 162px; top: 110px;
    font-family: "Heebo", sans-serif;
    font-weight: 300;
    font-size: 29px;
    line-height: 1;
    color: var(--ink-brown);
    white-space: nowrap;
  }
  .card-front__tagline {
    position: absolute;
    left: 172px; top: 142px;
    font-family: "Heebo", sans-serif;
    font-weight: 300;
    font-size: 19px;
    line-height: 1;
    color: #9c5a6c;
    white-space: nowrap;
  }

  .card-back__ornament {
    position: absolute;
    right: 0; top: 4px;
    width: 124px; height: 240px;
    border-radius: 50% 0 0 50%;
    background: linear-gradient(180deg, rgba(107,74,60,0.22), rgba(107,74,60,0.08));
  }
  .card-back__body {
    position: absolute;
    left: 33px; top: 30px;
    width: 330px;
    color: var(--back-ink);
    font-size: 13px;
    line-height: 16px;
  }
  .therapist { margin-bottom: 14px; }
  .therapist__name {
    font-family: "Pinyon Script", cursive;
    font-size: 25px;
    line-height: 30px;
    color: var(--back-ink);
    letter-spacing: 1px;
  }
  .therapist__focus, .practice__note {
    font-family: "PT Sans", sans-serif;
    font-style: italic;
    font-size: 11.5px;
    color: var(--back-cream);
  }
  .divider {
    width: 306px;
    border-top: 1.5px dashed var(--back-ink);
    margin: -6px 0 8px;
  }
  .practice__label { color: var(--back-cream); }
  .practice__note { color: var(--back-cream); }
</style>
</head>
<body>

  <span class="board-label board-label--logo">Logo</span>

  <section class="master-logo">
    <div class="logo-art" role="img" aria-label="Illustrated songbird perched on a curling floral branch"></div>
    <div class="logo-name">The Linden Clinic</div>
    <div class="logo-tagline">Psychotherapy and Counselling</div>
  </section>

  <span class="board-label board-label--front">Front</span>
  <span class="board-label board-label--back">Behind</span>

  <article class="card card--front">
    <div class="card-front__art" role="img" aria-label="Faint songbird and floral branch illustration"></div>
    <div class="card-front__name">The Linden Clinic</div>
    <div class="card-front__tagline">Psychotherapy and Counselling</div>
  </article>

  <article class="card card--back">
    <div class="card-back__ornament" role="img" aria-label="Curling floral vine ornament along the right edge"></div>
    <div class="card-back__body">
      <div class="therapist">
        <div class="therapist__name">Helen Marlow</div>
        <div class="therapist__focus">Postnatal Depression, Childbirth and Parenting Years Issues.</div>
        <div class="therapist__contact">07700 900 412 | info@helenmarlow-example.co.uk</div>
      </div>
      <div class="therapist">
        <div class="therapist__name">Rosa Penhale</div>
        <div class="therapist__focus">Confidence, bullying and childhood trauma.</div>
        <div class="therapist__contact">01632 960 318 or 07700 900 857 | info@corveltherapy-example.co.uk</div>
      </div>
      <div class="divider"></div>
      <div class="practice">
        <div class="practice__label">Our practice:</div>
        <div class="practice__address">12b Mill Lane Corvell. CV9 2QX | www.the-linden-clinic-example.co.uk</div>
        <div class="practice__note">(A short walk from the Minster)</div>
      </div>
    </div>
  </article>

</body>
</html>
```